An international wholesale business needs letterhead design

Logo file is attached. Please design a letterhead with the following details:

- Company Name and Logo
- Address
- VAT Registration number
- Phone No
- Website address

```html
<!DOCTYPE html>
<html lang="en">
<head>
<meta charset="utf-8">
<title>Veltora Trading Letterhead</title>
<link rel="stylesheet" href="https://fonts.googleapis.com/css2?family=Open+Sans:wght@400;600;700&display=swap">
<style>
  :root {
    --backdrop: #b5b6b8;
    --paper: #ffffff;
    --brand-red: #c4242f;
    --brand-grey: #8e9399;
    --ink: #3a3a3a;
    --ink-soft: #4a4a4a;
    --signature-tone: #ececee;
  }
  * { margin: 0; padding: 0; box-sizing: border-box; }
  html, body {
    width: 1200px; height: 900px; overflow: hidden;
    background: var(--backdrop);
    font-family: "Open Sans", Arial, sans-serif;
  }
  .letterhead {
    position: absolute; left: 336px; top: 107px;
    width: 527px; height: 682px;
    background: var(--paper);
    color: var(--ink);
  }
  .brand {
    position: absolute; left: 30px; top: 38px;
  }
  .brand-name {
    font-size: 21px; font-weight: 700; color: var(--brand-red);
    letter-spacing: 0.5px; line-height: 28px;
  }
  .contact {
    position: absolute; left: 383px; top: 30px;
    font-size: 8.8px; line-height: 12.4px; letter-spacing: 0.3px;
    color: var(--ink-soft); font-style: normal;
  }
  .contact-line { display: flex; align-items: center; gap: 3px; }
  .contact-line svg { width: 8px; height: 8px; fill: var(--brand-red); }
  .letter {
    position: absolute; left: 58px; top: 134px; width: 414px;
    font-size: 9.6px; line-height: 12.4px; letter-spacing: 0.45px;
  }
  .letter-date, .letter-greeting, .letter-closing, .letter-name {
    font-weight: 600; font-size: 10px; letter-spacing: 0.4px;
  }
  .letter-greeting { margin-top: 12px; }
  .letter-body p { text-align: justify; margin-top: 12px; }
  .letter-body p:first-child { margin-top: 18px; }
  .sign-off {
    position: absolute; left: 58px; top: 448px;
  }
  .signature {
    width: 195px; height: 36px; margin-top: 12px; margin-left: -3px;
    background: var(--signature-tone); border-radius: 4px;
  }
  .letter-name { margin-top: 16px; }
  .footer-band {
    position: absolute; left: 0; bottom: 0; width: 100%; height: 23px;
    display: flex;
  }
  .footer-grey { width: 107px; background: var(--brand-grey); }
  .footer-red {
    flex: 1; background: var(--brand-red);
    display: flex; align-items: center; justify-content: flex-end;
    padding-right: 33px;
    color: #fff; font-size: 7px; font-weight: 700; letter-spacing: 0.4px;
  }
</style>
</head>
<body>
  <main class="letterhead">
    <header>
      <div class="brand">
        <span class="brand-name">VELTORA TRADING</span>
      </div>
      <address class="contact">
        <div>420 Larkspur Plaza,</div>
        <div>Suite 118, MN 55409</div>
        <div class="contact-line">
          <svg viewBox="0 0 24 24" aria-hidden="true"><path d="M6.6 10.8a15.1 15.1 0 0 0 6.6 6.6l2.2-2.2a1 1 0 0 1 1-.25 11.4 11.4 0 0 0 3.6.57 1 1 0 0 1 1 1V20a1 1 0 0 1-1 1A17 17 0 0 1 3 4a1 1 0 0 1 1-1h3.5a1 1 0 0 1 1 1c0 1.250.2 2.450.57 3.57a1 1 0 0 1-.25 1z"/></svg>
          612-555-0148
        </div>
        <div class="contact-line">
          <svg viewBox="0 0 24 24" aria-hidden="true"><path d="M12 2a10 10 0 1 0 0 20 10 10 0 0 0 0-20zm6.9 6h-2.9a15.6 15.6 0 0 0-1.4-3.6A8 8 0 0 1 18.9 8zM12 4a14 14 0 0 1 1.9 4h-3.8A14 14 0 0 1 12 4zM4.3 14a8 8 0 0 1 0-4h3.4a16 16 0 0 0 0 4zm.8 2h2.9a15.6 15.6 0 0 0 1.4 3.6A8 8 0 0 1 5.1 16zM8 8H5.1a8 8 0 0 1 4.3-3.6A15.6 15.6 0 0 0 8 8zm4 12a14 14 0 0 1-1.9-4h3.8A14 14 0 0 1 12 20zm2.3-6H9.7a14.7 14.7 0 0 1 0-4h4.6a14.7 14.7 0 0 1 0 4zm.3 5.6a15.6 15.6 0 0 0 1.4-3.6h2.9a8 8 0 0 1-4.3 3.6zM16.3 14a16 16 0 0 0 0-4h3.4a8 8 0 0 1 0 4z"/></svg>
          www.veltoratrading.com
        </div>
      </address>
    </header>

    <article class="letter">
      <div class="letter-date">Monday, January 05, 2020</div>
      <div class="letter-greeting">Dear Madam/Sir</div>
      <div class="letter-body">
        <p>Lorem ipsum dolor sit amet, consectetur adipiscing elit, sed do eiusmod tempor incididunt ut labore et dolore magna aliqua. Ut enim ad minim veniam, quis nostrud exercitation ullamco laboris nisi ut aliquip ex ea commodo consequat. Duis aute irure dolor in reprehenderit in voluptate velit esse cillum dolore eu fugiat nulla pariatur. Excepteur sint occaecat cupidatat non proident, sunt in culpa qui officia deserunt mollit anim id est laborum.</p>
        <p>Curabitur pretium tincidunt lacus. Nulla gravida orci a odio. Nullam varius, turpis et commodo pharetra, est eros bibendum elit, nec luctus magna felis sollicitudin mauris. Integer in mauris eu nibh euismod gravida. Duis ac tellus et risus vulputate vehicula. Donec lobortis risus a elit. Etiam tempor. Ut ullamcorper, ligula eu tempor congue, eros est euismod turpis, id tincidunt sapien risus a quam. Maecenas fermentum consequat mi. Donec fermentum. Pellentesque malesuada nulla a mi. Duis sapien sem, aliquet nec, commodo eget, consequat quis, neque. Aliquam faucibus, elit ut dictum aliquet, felis nisl adipiscing sapien, sed malesuada diam lacus eget erat. Cras mollis scelerisque nunc. Nullam arcu. Aliquam consequat. Curabitur augue lorem, dapibus quis, laoreet et, pretium ac, nisi. Aenean magna nisl, mollis quis, molestie eu, feugiat in, orci. In hac habitasse platea dictumst.</p>
      </div>
    </article>

    <section class="sign-off">
      <div class="letter-closing">Sincerely,</div>
      <div class="signature" role="img" aria-label="Handwritten signature of Lian Corvell"></div>
      <div class="letter-name">Mr. Lian Corvell</div>
    </section>

    <footer class="footer-band">
      <div class="footer-grey"></div>
      <div class="footer-red">VAT REGISTRATION NUMBER</div>
    </footer>
  </main>
</body>
</html>
```